VMR business card

Need a business card for a company that provides instructional design and elearning development services. The website is here: http://vantmoro.studio/

I'm attaching a current logo, as well as the old business card design. While I like to keep it clean, the old design is too simplistic for my liking. The only idea I want to reuse from the old design is placing industry jargon on the back of the card, just need a better way to present it. But if you have other ideas for the back--feel free to experiment.

Please use the colors complementary to the color we have on the website. Thank you!

```html
<!DOCTYPE html>
<html lang="en">
<head>
<meta charset="utf-8">
<title>VMR business card</title>
<link rel="stylesheet" href="https://fonts.googleapis.com/css2?family=Lato:wght@400;700&family=Montserrat:wght@700&family=Roboto+Condensed:wght@700&display=swap">
<style>
  :root {
    --teal: #13b3b0;
    --gold: #dccd96;
    --card-dark: #2a2a2c;
    --paper: #ffffff;
    --backdrop: #e9e7e3;
  }
  html, body {
    margin: 0;
    padding: 0;
    width: 1138px;
    height: 1200px;
    overflow: hidden;
    background: var(--backdrop);
  }
  .canvas {
    position: relative;
    width: 1138px;
    height: 1200px;
  }
  .card {
    position: absolute;
    left: 150px;
    width: 838px;
    border-radius: 18px;
    overflow: hidden;
    box-shadow: 0 6px 18px rgba(0,0,0,0.25);
  }
  .card-front {
    top: 90px;
    height: 479px;
    background: var(--paper);
  }
  .card-back {
    top: 625px;
    height: 476px;
    background: var(--card-dark);
  }
  .front-field {
    position: absolute;
    inset: 0;
    width: 100%;
    height: 100%;
  }
  .brand-name {
    position: absolute;
    left: 62px;
    top: 170px;
    margin: 0;
    font-family: "Lato", sans-serif;
    font-weight: 700;
    font-size: 58px;
    letter-spacing: 4px;
    color: var(--teal);
  }
  .contact {
    position: absolute;
    right: 42px;
    top: 272px;
    text-align: right;
    font-family: "Lato", sans-serif;
    color: var(--paper);
  }
  .contact-name {
    margin: 0 0 30px 0;
    font-weight: 700;
    font-size: 25px;
  }
  .contact-line {
    display: flex;
    justify-content: flex-end;
    align-items: center;
    gap: 12px;
    margin: 0;
    font-size: 22px;
    line-height: 29px;
  }
  .contact-icon {
    width: 22px;
    height: 22px;
    flex: none;
  }
  .jargon {
    position: absolute;
    inset: 0;
    width: 100%;
    height: 100%;
  }
  .jargon-term {
    font-family: "Montserrat", sans-serif;
    font-weight: 700;
    font-size: 49px;
    fill: var(--teal);
  }
  .jargon-question {
    font-family: "Roboto Condensed", sans-serif;
    font-weight: 700;
    font-size: 90px;
    letter-spacing: -4px;
    fill: var(--paper);
  }
</style>
</head>
<body>
<main class="canvas">

  <section class="card card-front" aria-label="Card front">
    <svg class="front-field" viewBox="0 0 838 479" preserveAspectRatio="none" aria-hidden="true">
      <path d="M0,380 Q420,360 838,140 L838,479 L0,479 Z" fill="var(--teal)"/>
      <path d="M0,352 Q420,332 838,112" fill="none" stroke="var(--gold)" stroke-width="8"/>
    </svg>

    <h1 class="brand-name">VMR</h1>

    <div class="contact">
      <p class="contact-name">Dorian Halvesk</p>
      <p class="contact-line">555-013-2748
        <svg class="contact-icon" viewBox="0 0 24 24" aria-label="Phone"><path d="M7 3 L10 3 L11 8 L9 9.5 C10 12.5 11.5 14 14.5 15 L16 13 L21 14 L21 17 C21 19 19 21 17 21 C9 20 4 15 3 7 C3 5 5 3 7 3 Z" fill="var(--paper)"/></svg>
      </p>
      <p class="contact-line">dhalvesk@vantmoro.studio
        <svg class="contact-icon" viewBox="0 0 24 24" aria-label="Email"><rect x="2" y="5" width="20" height="14" fill="var(--paper)"/><path d="M2 5 L12 13 L22 5 M2 19 L9 11 M22 19 L15 11" fill="none" stroke="var(--teal)" stroke-width="1.6"/></svg>
      </p>
      <p class="contact-line">www.vantmoro.studio
        <svg class="contact-icon" viewBox="0 0 24 24" aria-label="Website"><g fill="none" stroke="var(--paper)" stroke-width="1.8"><circle cx="12" cy="12" r="9.5"/><ellipse cx="12" cy="12" rx="4.2" ry="9.5"/><path d="M2.5 12 H21.5 M4 7.5 H20 M4 16.5 H20"/></g></svg>
      </p>
    </div>
  </section>

  <section class="card card-back" aria-label="Card back">
    <svg class="jargon" viewBox="0 0 838 476" role="group" aria-label="Services">
      <text class="jargon-term" x="48" y="66" textLength="740" lengthAdjust="spacing">MOBILE LEARNING SCORM</text>
      <text class="jargon-term" x="48" y="126" textLength="740" lengthAdjust="spacing">INSTRUCTIONAL DESIGN LMS</text>
      <text class="jargon-term" x="48" y="186" textLength="740" lengthAdjust="spacing">MOOCS ELEARNING HTML5</text>

      <rect x="0" y="199" width="28" height="70" fill="var(--paper)"/>
      <rect x="810" y="199" width="28" height="70" fill="var(--paper)"/>
      <text class="jargon-question" x="48" y="267" textLength="740" lengthAdjust="spacingAndGlyphs">HOW CAN WE HELP?</text>

      <text class="jargon-term" x="52" y="323" textLength="740" lengthAdjust="spacing">ADULT LEARNING THEORY</text>
      <text class="jargon-term" x="52" y="384" textLength="740" lengthAdjust="spacing">GAMIFICATION CLASSROOM</text>
      <text class="jargon-term" x="52" y="444" textLength="742" lengthAdjust="spacing">XAPI BLENDED LEARNING</text>
    </svg>
  </section>

</main>
</body>
</html>
```